Branding product image: TOMBEL (Golden Papaya) in Plastic Cup (Ready to Eat)

The product is sliced Fruit in Light syrup
Flavour: TOMBEL (Golden Papaya)
The temporary product name: TOMBEL
I want the product design to be something 'fun', 'natural', and 'colourful'
The design concept could be anything depends on your imagination, but it must be eye catchy and attractive.
Basically, I want you to be creative in designing the logo and the overall graphic design for the label.
The measurement is 20 cm (Length) x 6,5 cm (Height)
The target customers are young and health conscious audiences (10 years - 65 years old).
Create something different. Something extraordinary.
Brief summary about the fruit:
This fruit only grows in certain part of the world. It grows in mountain area that is in tropical climate. The fruit flesh has a yellowish-golden color. It has an extraordinary taste (unlike normal papaya) and it suits very well with any dishes from cold appetizer, white/ red meat, desserts, and cocktails.
I need a packaging design for Fruit Cup productThe product is sliced Fruit in Light syrup.There will be various flavours i.e. apple, lychee, peach, papaya, etc.However, you may design the product using one sample flavour (i.e. papaya) first, as the designs of other flavours could be adjusted afterwards.The temporary product name is: RICCANAI want the product design to be something 'fun', 'natural', and 'colourful'.The design concept could be anything depends on your imagination. Basically, I want you to be creative in designing the logo and the overall graphic design for the label. - Create something different. Something extraordinary -Additional:The measurement is 20cm (Length) x 5cm (Height).The target customers are young audiences (10 years - 35 years old).The product design must stand out in the supermarket shelf.It must be eye catchy and attractive.Thank you,Harold-PLEASE REFER TO DESIGN SAMPLE ATTACHED TO HAVE A BETTER UNDERSTANDING FOR THE PRODUCT CONCEPT- Added Wednesday, September 17, 2014
Project Deadline Extended Reason: Haven't found a good design. Added Friday, September 19, 2014
Project Deadline Extended Reason: Need more time for designers to finalize and perfect the design.Thank you,Harold Added Monday, September 29, 2014
Project Deadline Extended Reason: I haven't found a great design yet. Added Tuesday, February 24, 2015
Reason: Getting better designs now. Still Open to new ideas while refining the latest designs from some designers.
Please do your best in submitting other great designs!

```html
<!DOCTYPE html>
<html lang="en">
<head>
<meta charset="utf-8">
<title>LUPEDOS Sliced Papaya Label</title>
<link href="https://fonts.googleapis.com/css2?family=Fredoka:wght@600&family=PT+Serif:wght@700&family=Arimo:wght@400&display=swap" rel="stylesheet">
<style>
  :root {
    --page-bg: #ffffff;
    --label-edge: #f39c1a;
    --label-mid: #fdc13a;
    --badge-white: #ffffff;
    --badge-ring: #d8232a;
    --brand-green: #7dbb2f;
    --ribbon-red: #d8232a;
    --ribbon-shade: #a5161c;
    --ribbon-text: #ffffff;
    --fruit-deep: #f06b1c;
    --fruit-light: #fb9a3c;
    --ink: #1a1a1a;
  }
  html, body {
    margin: 0;
    padding: 0;
    width: 1145px;
    height: 1200px;
    overflow: hidden;
    background: var(--page-bg);
  }
  .canvas {
    position: relative;
    width: 1145px;
    height: 1200px;
  }
  .label {
    position: absolute;
    left: 72px;
    top: 437px;
    width: 1000px;
    height: 326px;
    background: linear-gradient(90deg, var(--label-edge) 0%, var(--label-mid) 50%, var(--label-edge) 100%);
  }
  .badge {
    position: absolute;
    left: 50%;
    top: 50%;
    width: 312px;
    height: 312px;
    margin: -156px 0 0 -156px;
    box-sizing: border-box;
    border: 5px solid var(--badge-ring);
    border-radius: 50%;
    background: var(--badge-white);
  }
  .brand-name {
    position: absolute;
    top: 34px;
    left: 0;
    right: 0;
    text-align: center;
    font-family: "Fredoka", sans-serif;
    font-weight: 600;
    font-size: 54px;
    letter-spacing: 1px;
    color: var(--brand-green);
    line-height: 1;
  }
  .ribbon {
    position: absolute;
    top: 100px;
    left: 34px;
    width: 236px;
    height: 34px;
  }
  .ribbon-text {
    position: absolute;
    top: 106px;
    left: 34px;
    width: 236px;
    text-align: center;
    font-family: "PT Serif", serif;
    font-weight: 700;
    font-size: 16px;
    color: var(--ribbon-text);
    line-height: 20px;
  }
  .fruit-photo {
    position: absolute;
    top: 148px;
    left: 76px;
    width: 150px;
    height: 100px;
    border-radius: 50px 50px 40px 40px;
    background: radial-gradient(ellipse at 60% 45%, var(--fruit-light) 0%, var(--fruit-deep) 80%, rgba(240,107,28,0) 100%);
  }
  .net-weight {
    position: absolute;
    top: 262px;
    left: 0;
    right: 0;
    text-align: center;
    font-family: "Arimo", sans-serif;
    font-size: 15px;
    color: var(--ink);
  }
</style>
</head>
<body>
  <main class="canvas">
    <section class="label">
      <div class="badge">
        <div class="brand-name">LUPEDOS</div>
        <svg class="ribbon" viewBox="0 0 236 34" aria-hidden="true">
          <path d="M0 6 Q118 -2 236 4 L232 28 Q118 22 4 32 Z" fill="var(--ribbon-red)"/>
          <path d="M232 28 L236 4 L230 10 Z" fill="var(--ribbon-shade)"/>
        </svg>
        <div class="ribbon-text">Sliced in Light syrup</div>
        <div class="fruit-photo" role="img" aria-label="Photo of sliced golden papaya with seeds"></div>
        <div class="net-weight">NET WT 6 OZ (170g)</div>
      </div>
    </section>
  </main>
</body>
</html>
```